Dietitian needs a new business card design

I need a new business card design for my nutrition business that provides individual clinical nutrition advice for people with medical conditions. Business cards will be handed out to doctors, specialists and clients so will need to be sharp and project an image of professionalism

Target Market(s)

My clients are typically referred by doctors or specialists and the card will be used to handout to clients and their doctors.

Industry/Entity Type

Medical

Contact Information for Business Card

The business card will require the details below. These details can be found from my website https://www.kelvarrowclinic.com.au/

Font styles to use
Serif

Colors

Designer to choose colors to be used in the design.

Requirements
Must have
• 1. It needs be professional and contemporary
• 2. It needs to incorporate my logo
• 3. It needs space to write appointment times and dates
• 4. It needs to provide my phone number, fax number, email address and my web address
Nice to have
• Include the Registered Tovance Clinician Logo
• I have access to Framellow if required
• The locations I practise from
Should not have
• Pictures of food
• Spelling MIstakes

```html
<!DOCTYPE html>
<html lang="en">
<head>
<meta charset="utf-8">
<title>Kelvarrow Nutrition &amp; Dietetics – Business Card</title>
<link rel="stylesheet" href="https://fonts.googleapis.com/css2?family=Cinzel:wght@500&family=Marcellus&family=Tinos&display=swap">
<style>
  :root {
    --navy: #1b2f95;
    --blue: #1d4ea8;
    --green: #a2d418;
    --orange: #de6522;
    --badge-orange: #ee7425;
    --stripe: #f3f3f3;
    --grey-band: #cccccc;
    --ink: #1e1e1e;
    --frame: #9a9a9a;
    --page: #ffffff;
  }
  * { box-sizing: border-box; margin: 0; padding: 0; }
  html, body { width: 1200px; height: 1200px; overflow: hidden; background: var(--page); }
  .sheet {
    position: relative; width: 1200px; height: 1200px;
    border: 2px solid #444; background: var(--page);
    font-family: "Marcellus", serif; color: var(--ink);
  }
  .side-label {
    position: absolute; font-family: Arial, Helvetica, sans-serif;
    font-size: 17px; color: #333; letter-spacing: 0.3px;
  }
  .side-label--front { top: 82px; right: 180px; }
  .side-label--back { top: 612px; left: 177px; }

  .card {
    position: absolute; left: 180px; width: 838px; height: 480px;
    border: 1px solid var(--frame); overflow: hidden; background: #fff;
  }
  .card--front { top: 106px; }
  .card--back { top: 636px; }

  /* front */
  .front__tint { position: absolute; left: 6px; right: 6px; background: var(--stripe); }
  .front__tint--top { top: 3px; height: 91px; }
  .front__tint--bottom { top: 293px; height: 100px; }
  .front__green { position: absolute; left: 0; right: 0; top: 418px; bottom: 0; background: var(--green); }
  .front__orange { position: absolute; top: 392px; height: 51px; width: 190px; background: var(--orange); }
  .front__orange--left { left: 0; }
  .front__orange--right { right: 0; }
  .front__web-panel {
    position: absolute; left: 190px; right: 190px; top: 380px; height: 38px; background: #fff;
  }
  .front__web {
    position: absolute; left: 0; right: 0; top: 382px; text-align: center;
    font-family: "Tinos", serif; font-size: 27px; letter-spacing: 1.6px; color: #111;
  }
  .brand {
    position: absolute; left: 0; right: 0; top: 164px;
    display: flex; align-items: center; justify-content: center; gap: 22px;
  }
  .brand__dot { width: 78px; height: 78px; border-radius: 50%; background: var(--blue); }
  .brand__name { font-family: "Marcellus", serif; font-size: 34px; color: var(--navy); }

  /* back */
  .back__top-band { position: absolute; left: 0; right: 0; top: 0; height: 26px; background: var(--grey-band); }
  .appointment {
    position: absolute; left: 68px; top: 56px; width: 354px; height: 59px;
    border: 2px solid #333; display: flex; align-items: center; justify-content: center;
    font-family: "Cinzel", serif; font-size: 38px; font-weight: 500; letter-spacing: 3px; color: #222;
  }
  .slot { position: absolute; left: 539px; font-size: 22px; color: #222; white-space: nowrap; }
  .slot--date { top: 53px; }
  .slot--time { top: 95px; }
  .back__contact-band { position: absolute; left: 0; right: 0; top: 333px; bottom: 0; background: var(--grey-band); }
  .back__halo { position: absolute; left: 544px; top: 239px; width: 314px; height: 314px; border-radius: 50%; background: #fff; }
  .back__mark { position: absolute; left: 565px; top: 260px; width: 272px; height: 272px; border-radius: 50%; background: var(--blue); }
  .cert-badge { position: absolute; left: 599px; top: 351px; width: 194px; height: 92px; border-radius: 3px; background: var(--badge-orange); }
  .contact { position: absolute; display: flex; align-items: center; font-size: 27px; color: #111; white-space: nowrap; }
  .contact svg { position: absolute; left: -30px; }
  .contact--phone { left: 77px; top: 363px; }
  .contact--fax { left: 301px; top: 363px; }
  .contact--email { left: 77px; top: 399px; }
</style>
</head>
<body>
<div class="sheet">
  <div class="side-label side-label--front">FRONT</div>
  <section class="card card--front">
    <div class="front__tint front__tint--top"></div>
    <div class="front__tint front__tint--bottom"></div>
    <div class="brand">
      <div class="brand__dot"></div>
      <div class="brand__name">Kelvarrow Nutrition &amp; Dietetics</div>
    </div>
    <div class="front__green"></div>
    <div class="front__orange front__orange--left"></div>
    <div class="front__orange front__orange--right"></div>
    <div class="front__web-panel"></div>
    <div class="front__web">www.kelvarrowclinic.com.au</div>
  </section>

  <div class="side-label side-label--back">BACK</div>
  <section class="card card--back">
    <div class="back__top-band"></div>
    <div class="appointment">APPOINTMENT</div>
    <div class="slot slot--date">DATE : __________________</div>
    <div class="slot slot--time">TIME : __________________</div>
    <div class="back__contact-band"></div>
    <div class="back__halo"></div>
    <div class="back__mark"></div>
    <div class="cert-badge" role="img" aria-label="Registered Tovance Clinician badge"></div>

    <div class="contact contact--phone">
      <svg width="16" height="24" viewBox="0 0 16 24" aria-hidden="true"><path d="M5 1h4l1 6-3 2c0 3 1 5 3 7l3-1 2 5-3 3C6 22 2 15 2 8 2 5 3 2 5 1z" fill="#111"/></svg>
      0400 555 218
    </div>
    <div class="contact contact--fax">
      <svg width="20" height="18" viewBox="0 0 20 18" aria-hidden="true"><rect x="5" y="1" width="10" height="5" fill="#111"/><rect x="1" y="6" width="18" height="8" rx="1" fill="#111"/><rect x="5" y="11" width="10" height="6" fill="#fff" stroke="#111" stroke-width="1.5"/></svg>
      +613 5550 1472
    </div>
    <div class="contact contact--email">
      <svg width="20" height="15" viewBox="0 0 20 15" aria-hidden="true"><rect x="0" y="1" width="20" height="14" rx="1" fill="#111"/><path d="M0 2l10 7 10-7" fill="none" stroke="#ccc" stroke-width="1.6"/></svg>
      reception@kelvarrowclinic.com.au
    </div>
  </section>
</div>
</body>
</html>
```